Veracor Systems
Business Cards
Veracor Systems - Information Technology
Creative Brief
Professional
Martin Osgood
Vice President
Veracor IT Systems Harbourline Tower 482 Dunmore Ave East,Suite 3100 Toronto ON, M4R 2T7
martin.osgood@veracorsystems-example.ca
www.veracorsystems-example.ca

```html
<!DOCTYPE html>
<html lang="en">
<head>
<meta charset="utf-8">
<title>Veracor Systems – Business Cards</title>
<link href="https://fonts.googleapis.com/css2?family=Roboto:wght@400;500;700;900&display=swap" rel="stylesheet">
<style>
  :root{
    --backdrop:#e6e4e1;
    --card:#ffffff;
    --brand-blue:#2ba2d8;
    --brand-blue-dark:#1b7fb3;
    --swoosh-grey:#7a7c80;
    --text:#5a5b5e;
    --text-soft:#7d7f83;
    --rule:#b9bbbe;
  }
  *{margin:0;padding:0;box-sizing:border-box;}
  html,body{width:1200px;height:852px;overflow:hidden;}
  body{background:var(--backdrop);font-family:"Roboto",Arial,sans-serif;position:relative;color:var(--text);}

  .card{position:absolute;width:560px;height:320px;background:var(--card);border-radius:16px;overflow:hidden;box-shadow:0 6px 18px rgba(0,0,0,.18);}
  .card--front{left:40px;top:110px;}
  .card--back{left:600px;top:420px;}

  .swoosh{position:absolute;left:0;top:0;width:560px;height:320px;}

  .brand-mark{position:absolute;display:flex;align-items:center;}
  .brand-square{background:var(--brand-blue);border-radius:6px;flex:none;}
  .brand-name{color:var(--brand-blue-dark);font-weight:900;text-transform:uppercase;letter-spacing:.5px;line-height:1;}

  .card--front .brand-mark{left:80px;top:80px;width:180px;flex-direction:column;gap:18px;}
  .card--front .brand-square{width:62px;height:62px;}
  .card--front .brand-name{font-size:19px;text-align:center;}

  .card--back .brand-mark{left:190px;top:44px;gap:14px;}
  .card--back .brand-square{width:50px;height:50px;}
  .card--back .brand-name{font-size:24px;}

  .divider{position:absolute;width:1px;background:var(--rule);}
  .card--front .divider{left:268px;top:40px;height:240px;}
  .card--back .divider{left:292px;top:140px;height:150px;}

  .person-name{color:var(--brand-blue);font-weight:500;font-size:17px;}
  .person-title{color:var(--text-soft);font-size:12.5px;}
  .address{font-size:12px;line-height:1.45;color:var(--text);}

  .contact-list{list-style:none;font-size:11.5px;color:var(--text);}
  .contact-list li{display:flex;align-items:center;gap:8px;margin-bottom:5px;white-space:nowrap;}
  .contact-list svg{width:12px;height:12px;flex:none;}

  .card--front .person-block{position:absolute;left:284px;top:42px;}
  .card--front .person-title{margin-top:4px;}
  .card--front .address{position:absolute;left:284px;top:122px;}
  .card--front .contact-list{position:absolute;left:284px;top:190px;}

  .card--back .person-block{position:absolute;left:60px;top:150px;width:224px;text-align:center;}
  .card--back .person-name{font-size:19px;margin-bottom:10px;}
  .card--back .person-title{position:absolute;left:308px;top:146px;font-weight:700;color:var(--text);font-size:13px;}
  .card--back .contact-list{position:absolute;left:308px;top:172px;}
</style>
</head>
<body>

<section class="card card--front" aria-label="Business card, front">
  <svg class="swoosh" viewBox="0 0 560 320" aria-hidden="true">
    <path d="M0,62 C44,120 58,220 40,320 L0,320 Z" fill="var(--brand-blue)"/>
    <path d="M0,50 C56,112 74,214 56,320 L48,320 C64,214 48,118 0,62 Z" fill="var(--swoosh-grey)"/>
  </svg>
  <div class="brand-mark">
    <span class="brand-square"></span>
    <span class="brand-name">Veracor IT Systems</span>
  </div>
  <span class="divider"></span>
  <div class="person-block">
    <p class="person-name">Martin Osgood</p>
    <p class="person-title">Vice President</p>
  </div>
  <p class="address">Harbourline Tower<br>482 Dunmore Ave East,Suite 3100<br>Toronto ON, M4R 2T7</p>
  <ul class="contact-list">
    <li><svg viewBox="0 0 12 12"><path d="M3 1 L5 3.5 L4 5 C4.8 6.6 5.6 7.4 7 8 L8.5 7 L11 9 L9.6 11 C5 10.5 1.5 7 1 2.4 Z" fill="var(--brand-blue)"/></svg>1 (416) 555-0142</li>
    <li><svg viewBox="0 0 12 12"><rect x="1" y="2.5" width="10" height="7" rx="1" fill="var(--brand-blue)"/><path d="M1.5 3 L6 6.5 L10.5 3" stroke="#fff" stroke-width="1" fill="none"/></svg>martin.osgood@veracorsystems-example.ca</li>
    <li><svg viewBox="0 0 12 12"><circle cx="6" cy="6" r="5" fill="var(--brand-blue)"/><path d="M1 6 H11 M6 1 C3.5 4 3.5 8 6 11 M6 1 C8.5 4 8.5 8 6 11" stroke="#fff" stroke-width=".8" fill="none"/></svg>www.veracorsystems-example.ca</li>
  </ul>
</section>

<section class="card card--back" aria-label="Business card, back">
  <svg class="swoosh" viewBox="0 0 560 320" aria-hidden="true">
    <path d="M0,110 C36,170 46,250 30,320 L0,320 Z" fill="var(--brand-blue)"/>
    <path d="M0,96 C48,162 60,248 44,320 L36,320 C50,248 38,172 0,110 Z" fill="var(--swoosh-grey)"/>
  </svg>
  <div class="brand-mark">
    <span class="brand-square"></span>
    <span class="brand-name">Veracor IT Systems</span>
  </div>
  <div class="person-block">
    <p class="person-name">Martin Osgood</p>
    <p class="address">Harbourline Tower<br>482 Dunmore Ave East,Suite 3100<br>Toronto ON, M4R 2T7</p>
  </div>
  <span class="divider"></span>
  <p class="person-title">Vice President</p>
  <ul class="contact-list">
    <li><svg viewBox="0 0 12 12"><path d="M3 1 L5 3.5 L4 5 C4.8 6.6 5.6 7.4 7 8 L8.5 7 L11 9 L9.6 11 C5 10.5 1.5 7 1 2.4 Z" fill="var(--brand-blue)"/></svg>1 (416) 555-0142</li>
    <li><svg viewBox="0 0 12 12"><rect x="1" y="2.5" width="10" height="7" rx="1" fill="var(--brand-blue)"/><path d="M1.5 3 L6 6.5 L10.5 3" stroke="#fff" stroke-width="1" fill="none"/></svg>martin.osgood@veracorsystems-example.ca</li>
    <li><svg viewBox="0 0 12 12"><circle cx="6" cy="6" r="5" fill="var(--brand-blue)"/><path d="M1 6 H11 M6 1 C3.5 4 3.5 8 6 11 M6 1 C8.5 4 8.5 8 6 11" stroke="#fff" stroke-width=".8" fill="none"/></svg>www.veracorsystems-example.ca</li>
  </ul>
</section>

</body>
</html>
```